Tradeshow Exhibit Background Design

Looking to make improvements on my tradeshow exhibit backdrop. I created the current design myself, and I'm not 100% happy with it. Because its a big investment, I want it to be perfect.
For context:
- The booth will be used in multiple configurations (20 ft, 10 ft, and 8 ft).
- The booth structure will include two panels that are 5' x 7.5', and one panel that is 8' x 8.5' (attached a photo of the set-up.)
- We plan on getting the double sided fabric printing so that we can use it in the various configurations (the 10' config will be the two 5' panels put together, and the 20' config will be all three.)
The design should be visually impactful from a distance but also clear and readable up close. It needs to align with our brand identity and effectively communicate what we do at a glance.
I've includes a photo example of the booth structure, my current design, as well as our company brand guidelines.

```html
<!DOCTYPE html>
<html lang="en">
<head>
<meta charset="UTF-8">
<title>Keystone Tradeshow Backdrop – 10 ft Configuration</title>
<link rel="preconnect" href="https://fonts.googleapis.com">
<link href="https://fonts.googleapis.com/css2?family=Saira+Semi+Condensed:wght@600;700&family=Open+Sans:wght@400&display=swap" rel="stylesheet">
<style>
  :root {
    --page-bg: #ffffff;
    --brand-blue: #365eab;
    --brand-red: #d2292f;
    --slate-grey: #7b878b;
    --mist-grey: #c7d0dc;
    --photo-dark: #0d1014;
    --photo-mid: #4a5668;
    --photo-light: #a8b4c6;
    --photo-warm: #b3512a;
    --measure-line: #c6ced8;
    --measure-text: #2f3a44;
    --text-light: #ffffff;
  }

  * { margin: 0; padding: 0; box-sizing: border-box; }

  html, body {
    width: 1200px;
    height: 672px;
    overflow: hidden;
    background: var(--page-bg);
  }

  .canvas {
    position: relative;
    width: 1200px;
    height: 672px;
  }

  .backdrop {
    position: absolute;
    left: 274px;
    top: 161px;
    width: 483px;
    height: 361px;
    overflow: hidden;
  }

  .backdrop-photo {
    position: absolute;
    inset: 0;
    background:
      radial-gradient(ellipse 22% 20% at 54% 40%, var(--photo-warm) 0%, rgba(179,81,42,0) 100%),
      radial-gradient(ellipse 45% 55% at 50% 50%, var(--photo-light) 0%, var(--photo-mid) 55%, var(--photo-dark) 100%);
  }

  .backdrop-shapes {
    position: absolute;
    inset: 0;
    width: 100%;
    height: 100%;
  }

  .shape-blue { fill: var(--brand-blue); }
  .shape-red { fill: var(--brand-red); }
  .shape-slate { fill: var(--slate-grey); }
  .shape-mist { fill: var(--mist-grey); }

  .tagline {
    position: absolute;
    left: 32px;
    top: 46px;
    font-family: "Saira Semi Condensed", sans-serif;
    font-weight: 600;
    font-size: 18px;
    line-height: 20px;
    letter-spacing: 0.1px;
    color: var(--text-light);
    text-transform: uppercase;
  }

  .brand-name {
    position: absolute;
    left: 316px;
    top: 45px;
    width: 146px;
    text-align: center;
    font-family: "Saira Semi Condensed", sans-serif;
    font-weight: 700;
    font-size: 26px;
    line-height: 30px;
    letter-spacing: 1px;
    color: var(--text-light);
    text-transform: uppercase;
  }

  .measure {
    position: absolute;
    inset: 0;
    width: 1200px;
    height: 672px;
    pointer-events: none;
  }

  .measure-line {
    stroke: var(--measure-line);
    stroke-width: 2.5;
    fill: none;
    stroke-linecap: round;
  }

  .measure-label {
    position: absolute;
    font-family: "Open Sans", sans-serif;
    font-weight: 400;
    font-size: 18px;
    line-height: 20px;
    color: var(--measure-text);
    letter-spacing: 0.5px;
  }

  .label-height { left: 928px; top: 335px; }
  .label-left-width { left: 419px; top: 627px; }
  .label-right-width { left: 711px; top: 627px; }
</style>
</head>
<body>
<main class="canvas">

  <section class="backdrop" aria-label="Backdrop panel">
    <div class="backdrop-photo" role="img" aria-label="Photograph of a worker in an orange hard hat looking into a lit industrial control room"></div>

    <svg class="backdrop-shapes" viewBox="0 0 483 361" preserveAspectRatio="none" aria-hidden="true">
      <ellipse class="shape-blue" cx="0" cy="0" rx="218" ry="163"/>
      <ellipse class="shape-red" cx="483" cy="0" rx="218" ry="163"/>
      <ellipse class="shape-slate" cx="0" cy="361" rx="218" ry="163"/>
      <ellipse class="shape-mist" cx="483" cy="361" rx="218" ry="163"/>
    </svg>

    <h1 class="tagline">Lasting gains,<br>proven results.</h1>
    <p class="brand-name">Keystone</p>
  </section>

  <svg class="measure" viewBox="0 0 1200 672" aria-hidden="true">
    <line class="measure-line" x1="923" y1="128" x2="923" y2="578"/>
    <line class="measure-line" x1="918" y1="128" x2="928" y2="128"/>
    <line class="measure-line" x1="918" y1="578" x2="928" y2="578"/>

    <line class="measure-line" x1="280" y1="612" x2="869" y2="612"/>
    <line class="measure-line" x1="280" y1="607" x2="280" y2="617"/>
    <line class="measure-line" x1="574" y1="607" x2="574" y2="617"/>
    <line class="measure-line" x1="869" y1="607" x2="869" y2="617"/>
  </svg>

  <span class="measure-label label-height">7.5'</span>
  <span class="measure-label label-left-width">5'</span>
  <span class="measure-label label-right-width">5'</span>

</main>
</body>
</html>
```